Brindle Works Australia Website

Brindle Works Australia (BWA) is a Industrial, Mining & Transport Services provider in Australia. We require a website that is both pc and mobile freindly. The website will be used to both present our company services and give us exposure in a crowded market. The main page of the website will have a snapshot of who BWA is and its from this page that the user can click to enter the area of interest ie. Industrial, Mining and Transport. A disticted logo can be used to indicate the area in question.<br/>Within the industrial, Mining and the Transport services pages will need list and description of services that are provided, current customer lists and news pages.<br/>The website will need a contacts page so prospective customers can get in contact with BWA.<br/>The website design will require a user freindly back end so future updates and ammendments can be carriedout by less experienced people within the BWA business.

Target Market(s)

Industrial, Mining and Transport Services provider markets

Coding

Coded - Design and coding required

Number of Pages Required

5+ page

Font styles to use
Sans Serif

Colors
00a990

Requirements
Must have
• Ability to build servises with in services. because the main service area is only the main service with in each service group there is alot of smaller services / tasks.
• Key wording for easy seach engine capabilities. The website will need to be search engine freindly.

```html
<!DOCTYPE html>
<html lang="en">
<head>
<meta charset="utf-8">
<title>Brindle Works Australia – About Us</title>
<link href="https://fonts.googleapis.com/css2?family=Montserrat:wght@400;500;600;700;800&family=Roboto+Condensed:wght@400;700&display=swap" rel="stylesheet">
<style>
:root{
  --green:#1d7d3f;
  --green-dark:#0f5a2a;
  --mission:#1f6a3a;
  --ink:#111;
  --text:#222;
  --muted:#555;
  --bar:#2b2b2b;
  --footer:#f1f1f1;
  --white:#fff;
}
*{margin:0;padding:0;box-sizing:border-box}
html,body{width:1200px;height:2298px;overflow:hidden;background:var(--white)}
body{position:relative;font-family:'Montserrat',sans-serif;color:var(--text)}
.abs{position:absolute}

/* header */
.site-header{position:absolute;left:0;top:0;width:1200px;height:112px;background:var(--white)}
.brand{position:absolute;left:125px;top:18px;display:flex;align-items:center;gap:10px}
.brand-mark{width:16px;height:16px;background:var(--green)}
.brand-name{font-weight:800;font-size:20px;line-height:1.05;color:var(--green);text-transform:uppercase;width:200px}
.brand-tag{position:absolute;left:125px;top:76px;font-size:10px;font-weight:700;color:var(--green);letter-spacing:.3px}
.call-bar{position:absolute;right:0;top:0;width:390px;height:42px;background:var(--bar);clip-path:polygon(0 0,100% 0,100% 100%,34px 100%)}
.call-bar span{position:absolute;left:50px;top:11px;color:var(--white);font-weight:600;font-size:14.5px;display:flex;align-items:center;gap:4px}
.main-nav a{position:absolute;top:65px;font-size:13.5px;font-weight:600;color:var(--ink);text-decoration:none;text-transform:uppercase}
.main-nav a.active{color:var(--green);padding-bottom:6px;border-bottom:2px solid #999}

/* hero */
.hero{position:absolute;left:0;top:112px;width:1200px;height:503px;background:linear-gradient(180deg,#9dbcdc 0%,#cfdeea 45%,#b8ab8e 60%,#8a7658 78%,#5a4a38 100%)}
.hero-box{position:absolute;left:119px;top:147px;width:353px;height:117px;background:var(--green);padding:31px 0 0 47px;color:var(--white)}
.hero-box .kicker{font-size:17px;font-weight:400;letter-spacing:.3px}
.hero-box h1{font-size:32px;font-weight:400;margin-top:3px;letter-spacing:.3px}
.hero-box h1 b{font-weight:700}

/* about */
.section-title{position:absolute;left:0;width:1200px;text-align:center;font-size:31px;font-weight:700;color:var(--ink)}
.title-rule{position:absolute;left:572px;width:56px;height:2px;background:#333}
.about-copy{position:absolute;left:155px;width:890px;text-align:center;font-size:15.5px;line-height:27px;color:var(--text)}

/* mission */
.mission{position:absolute;left:0;top:1022px;width:1200px;height:519px;background:linear-gradient(100deg,var(--mission) 0%,var(--mission) 55%,#24703f 78%,#1e5e33 100%)}
.mission-photo{position:absolute;left:110px;top:70px;width:430px;height:380px;border-radius:18px;background:linear-gradient(135deg,#3d5a6e 0%,#c9c83e 45%,#b8bf34 65%,#2f4a52 100%)}
.mission h2{position:absolute;left:600px;top:103px;font-size:31px;font-weight:700;color:var(--white)}
.mission p{position:absolute;left:605px;top:162px;width:500px;font-size:15.5px;line-height:27px;color:#e8f0ea}

/* team */
.member{position:absolute;top:1685px;width:206px;text-align:center}
.member-photo{width:206px;height:252px;clip-path:polygon(50% 0,100% 25%,100% 75%,50% 100%,0 75%,0 25%);background:linear-gradient(180deg,#d6d9db 0%,#bfc3c6 35%,#4a5060 65%,#1f2430 100%)}
.member h3{margin-top:22px;font-family:'Roboto Condensed',sans-serif;font-weight:700;font-size:15px;color:var(--ink);text-transform:uppercase}
.member p{margin-top:6px;font-size:12.5px;line-height:16px;color:var(--muted)}
.member .btn{display:inline-block;margin-top:14px;width:87px;height:28px;line-height:28px;background:var(--green);color:var(--white);font-family:'Roboto Condensed',sans-serif;font-weight:700;font-size:12.5px;text-decoration:none;border-radius:2px}

/* footer */
.site-footer{position:absolute;left:0;top:2145px;width:1200px;height:153px;background:var(--footer)}
.footer-nav a{position:absolute;top:62px;font-size:13.5px;font-weight:600;color:#333;text-decoration:none;text-transform:uppercase}
.copyright{position:absolute;left:154px;top:95px;font-size:12.5px;color:#444}
.social{position:absolute;top:49px;width:31px;height:31px;border-radius:50%;background:var(--ink)}
</style>
</head>
<body>

<header class="site-header">
  <div class="brand"><span class="brand-mark"></span><span class="brand-name">Brindle Works Australia</span></div>
  <div class="brand-tag">MINING AND TRANSPORT SERVICES</div>
  <div class="call-bar"><span>
    <svg width="14" height="14" viewBox="0 0 24 24"><path fill="#fff" d="M6.6 10.8a15 15 0 0 0 6.6 6.6l2.2-2.2c.3-.3.7-.4 1-.2 1.1.4 2.3.6 3.6.6.6 0 1 .4 1 1V20c0 .6-.4 1-1 1A17 17 0 0 1 3 4c0-.6.4-1 1-1h3.5c.6 0 1 .4 1 1 0 1.3.2 2.5.6 3.6.1.3 0 .7-.2 1z"/></svg>
    CALL US (600)&nbsp; 555 0182</span></div>
  <nav class="main-nav">
    <a style="left:434px" href="#">Home</a>
    <a class="active" style="left:524px" href="#">About Us</a>
    <a style="left:643px" href="#">Our Services</a>
    <a style="left:794px" href="#">News</a>
    <a style="left:882px" href="#">Blogs</a>
    <a style="left:976px" href="#">Contact Us</a>
  </nav>
</header>

<section class="hero" role="img" aria-label="Yellow mining haul truck on an open-cut mine site under a blue sky">
  <div class="hero-box">
    <div class="kicker">WHO WE ARE</div>
    <h1><b>ABOUT</b> BWA</h1>
  </div>
</section>
<svg class="abs" style="left:0;top:512px" width="1200" height="106" viewBox="0 0 1200 106">
  <polygon points="0,103 0,96 605,9 1200,95 1200,103 605,28" fill="var(--green-dark)"/>
  <polygon points="0,103 605,28 1200,103 1200,106 0,106" fill="#fff"/>
</svg>

<h2 class="section-title" style="top:624px">ABOUT US</h2>
<div class="title-rule" style="top:671px"></div>
<p class="about-copy" style="top:709px">Fusce tellus Sed metus augue convallis et vehicula ut pulvinar eu ante Integer orci tellus tristique vitae consequat nec porta vel lectus Nulla sit amet&nbsp; aliquam enim Proin dui lectus cursus Nunc tempus felis vitae urna Vivamus porttitor neque at volutpat rutrum purus nisi eleifend libero a tempus libero lectus</p>
<p class="about-copy" style="top:820px">Aeugiat felis Morbi diam mauris viverra in gravida eu mattis in ante Morbi eget arcu Morbi porta libero id ullamcorper nonummy nibh ligula pulvinar metus eget consectetuer augue nisi quis lacus Ut ac mi quis lacus mollis aliquam Curabitur iaculis tempus eros Curabitur vel mi sit amet magna malesuada</p>

<section class="mission">
  <div class="mission-photo" role="img" aria-label="Photo of two engineers in hi-vis gear and hard hats using a tablet and screen"></div>
  <h2>OUR MISSION</h2>
  <p>Nunc tempus felis vitae urna Vivamus porttitor neque at volutpat rutrum purus nisi eleifend libero a tempus libero lectus feugiat felis Morbi diam mauris viverra in gravida eu mattis in ante Morbi eget arcu Morbi porta libero id ullamcorper nonummy nibh ligula pulvinar metus eget consectetuer augue nisi quis lacus Ut ac mi quis lacus mollis aliquam Curabitur iaculis tempus eros Curabitur vel mi sit amet magn</p>
</section>

<h2 class="section-title" style="top:1619px">OUR TEAM</h2>
<div class="title-rule" style="top:1665px"></div>

<div class="member" style="left:135px">
  <div class="member-photo" role="img" aria-label="Portrait of team member in dark shirt, arms crossed"></div>
  <h3>Dorian</h3><p>Lorem ipsum dolor sit<br>amet consectetur</p><a class="btn" href="#">VIEW BIO</a>
</div>
<div class="member" style="left:367px">
  <div class="member-photo" role="img" aria-label="Portrait of team member in navy suit, arms crossed"></div>
  <h3>Leon Harte</h3><p>Lorem ipsum dolor sit<br>amet consectetur</p><a class="btn" href="#">VIEW BIO</a>
</div>
<div class="member" style="left:600px">
  <div class="member-photo" style="background:linear-gradient(180deg,#d8cec3 0%,#c2b6a8 35%,#5c87b8 65%,#3d6a9e 100%)" role="img" aria-label="Portrait of team member in blue check shirt, arms crossed"></div>
  <h3>Calvo</h3><p>Lorem ipsum dolor sit<br>amet consectetur</p><a class="btn" href="#">VIEW BIO</a>
</div>
<div class="member" style="left:831px">
  <div class="member-photo" role="img" aria-label="Portrait of team member in black blazer, arms crossed"></div>
  <h3>Mira Vance</h3><p>Lorem ipsum dolor sit<br>amet consectetur</p><a class="btn" href="#">VIEW BIO</a>
</div>

<footer class="site-footer">
  <nav class="footer-nav">
    <a style="left:154px" href="#">Home</a>
    <a style="left:243px" href="#">About Us</a>
    <a style="left:362px" href="#">Our Services</a>
    <a style="left:514px" href="#">News</a>
    <a style="left:602px" href="#">Blogs</a>
    <a style="left:695px" href="#">Contact Us</a>
  </nav>
  <div class="copyright">© 2020 Company Name | All Rights Reserved | Disclaimer</div>
  <a class="social" style="left:925px" href="#" aria-label="Social profile"></a>
  <a class="social" style="left:971px" href="#" aria-label="Social profile"></a>
  <a class="social" style="left:1015px" href="#" aria-label="Social profile"></a>
</footer>

</body>
</html>
```